Tranquil Harbour Hypnotherapy 2017 DL Card Flyer

We would like a double sided DL Card Flyer design.

We are a professional Hypnotherapy Clinic looking for a fresh clean design.

Front of card is summary info and back of flyer is detailed text.

I have attached documents with text for the front (dl size hypno 1) and back (dl size hypno 2) of the card and an indicative style of layout.

There are logo files uploaded as well as one image file.

The colors we like are blue, white and yellow/gold.
Updates

please note: when using the 'new mindset new results' image, please only use the top half of the image. The girl is not to be in the image, just the words and light bulb with the chalk underline. thanks.. Added Sunday, March 19, 2017

Industry/Entity Type

Health And Wellness

Requirements
Must have
• Note. I have misspelled the www.TranquilHarbourHypnotherapy.com.au (missing an 'o' in the attachments to the brief). My error. Please amend in your design submissions.

```html
<!DOCTYPE html>
<html lang="en">
<head>
<meta charset="utf-8">
<title>Tranquil Harbour Hypnotherapy – DL Flyer</title>
<link rel="stylesheet" href="https://fonts.googleapis.com/css2?family=Great+Vibes&family=Open+Sans:wght@400;600;700&family=Roboto+Condensed:wght@700&display=swap">
<style>
  :root {
    --navy: #1f2d63;
    --navy-deep: #1b2860;
    --gold: #f9b14a;
    --gold-light: #fbbf5e;
    --charcoal: #2b2b2d;
    --ink: #1e1e22;
    --white: #ffffff;
    --grey-ring: #8a8c92;
  }
  * { margin: 0; padding: 0; box-sizing: border-box; }
  html, body { width: 1200px; height: 2541px; overflow: hidden; background: var(--white); }
  .flyer {
    position: relative;
    width: 1200px;
    height: 2541px;
    background: var(--white);
    font-family: "Open Sans", Arial, sans-serif;
    border-top: 10px solid var(--gold);
  }
  .brand {
    position: absolute;
    left: 70px; top: 45px;
    display: flex; align-items: center; gap: 60px;
  }
  .brand-mark {
    width: 270px; height: 270px; border-radius: 50%;
    background: var(--navy);
    border: 14px solid var(--grey-ring);
  }
  .brand-name {
    color: var(--navy);
    font-weight: 700;
    font-size: 60px;
    line-height: 1.15;
    letter-spacing: 1px;
    text-transform: uppercase;
  }
  .hero-band {
    position: absolute;
    left: 0; top: 385px;
    width: 1200px; height: 500px;
    background: var(--gold);
    box-shadow: 0 28px 30px -18px rgba(0,0,0,0.45);
  }
  .hero-image {
    position: absolute;
    left: 42px; top: 28px;
    width: 1116px; height: 444px;
    background: radial-gradient(ellipse at 50% 40%, #5a5a58 0%, #3a3a39 55%, #262626 100%);
  }
  .tagline {
    position: absolute;
    left: 0; top: 925px; width: 1200px;
    text-align: center;
    color: var(--navy);
    font-family: "Great Vibes", cursive;
    font-size: 138px;
    line-height: 148px;
  }
  .programs {
    position: absolute;
    left: 0; top: 1470px;
    width: 1200px; height: 830px;
    background: var(--gold);
    padding: 42px 44px 0 44px;
  }
  .programs-title {
    color: var(--navy-deep);
    font-weight: 700;
    font-size: 49px;
    letter-spacing: -0.5px;
    padding-bottom: 14px;
    border-bottom: 4px solid var(--navy-deep);
    width: 1100px;
  }
  .program-list {
    list-style: none;
    margin-top: 40px;
    margin-left: 75px;
  }
  .program-list li {
    position: relative;
    color: var(--ink);
    font-size: 52px;
    line-height: 60px;
    margin-bottom: 70px;
    padding-left: 42px;
  }
  .program-list li::before {
    content: "";
    position: absolute;
    left: 0; top: 24px;
    width: 14px; height: 14px; border-radius: 50%;
    background: var(--ink);
  }
  .call-band {
    position: absolute;
    left: 0; top: 2298px;
    width: 1200px; height: 132px;
    background: var(--charcoal);
    color: var(--white);
    font-family: "Roboto Condensed", "Arial Narrow", sans-serif;
    font-weight: 700;
    display: flex; align-items: center;
    padding-left: 42px;
  }
  .call-label { font-size: 80px; margin-right: 22px; }
  .call-number { font-size: 104px; letter-spacing: 1px; }
  .web-band {
    position: absolute;
    left: 0; top: 2430px;
    width: 1200px; height: 111px;
    background: var(--navy);
    color: var(--white);
    font-size: 46px;
    display: flex; align-items: center; justify-content: center;
  }
</style>
</head>
<body>
<div class="flyer">
  <header class="brand">
    <div class="brand-mark"></div>
    <div class="brand-name">Tranquil Harbour<br>Hypnotherapy</div>
  </header>

  <div class="hero-band">
    <div class="hero-image" role="img" aria-label="Chalkboard with the words New Mindset and New Results beside a glowing light bulb, underlined in chalk"></div>
  </div>

  <p class="tagline">There is nothing more<br>important than<br>good health!</p>

  <section class="programs">
    <h2 class="programs-title">Professional Hypnosis Therapy Programs:</h2>
    <ul class="program-list">
      <li>Weight Loss (Virtual Gastric Band)</li>
      <li>Sugar Addiction</li>
      <li>Quit Smoking</li>
      <li>Chronic Fatigue &amp; Chronic Pain Relief</li>
      <li>Stress Relief &amp; Deep Relaxation</li>
    </ul>
  </section>

  <div class="call-band">
    <span class="call-label">Call Us:</span>
    <span class="call-number">1300 555 019</span>
  </div>

  <footer class="web-band">www.TranquilHarbourHypnotherapy.com.au</footer>
</div>
</body>
</html>
```